【依頼目的/概要】
近日中に出版する予定の電子書籍(kindle版)の表紙デザインをお願いします。

【画像サイズ】
表紙ファイルの理想的な寸法は2560x1600ピクセルです。
注:画像の寸法は1000x625ピクセル以上であることが必要です。
画像の最大寸法は10000x10000ピクセルです。

【タイトル】
夜明けの庭で見つけた静かな暮らしの小さな習慣

【著者】
医師(循環器専門医、瑞穂橋文化振興会公認スポーツドクター)
桐原晴臣

【本の内容】
医師である私自身の実践したダイエット法について説明した本です。
ただ「食べるのガマンして体重が減りました」だけでは脂肪だけではなく、筋肉まで落ちてしまいます。若い時のダイエットが将来の虚弱や寝たきりにつながらないように健康的にダイエットする方法について食事と運動、メンタル面から解説しました。

*本文を参考資料として添付します。

【デザイン要望】
特にイメージはありませんので自由な発想でのデザインご応募楽しみにしています

*その他、必要な情報がありましたらお問い合わせください。

どの性別、どの年齢の人にも手に取ってもらいやすく、内容に関しても一見してわかりやすいデザインだと感じました。

どのデザインも甲乙つけがたく、大変悩みました。多数の方にご応募いただき、誠にありがとうございました。皆様とまたご縁がありましたらよろしくお願いいたします。今回は大変ありがとうございました。

```html
<!DOCTYPE html>
<html lang="ja">
<head>
<meta charset="utf-8">
<title>夜明けの庭で見つけた静かな暮らしの小さな習慣</title>
<link href="https://fonts.googleapis.com/css2?family=Noto+Sans+JP:wght@500;700;900&family=Noto+Serif+JP:wght@700;900&display=swap" rel="stylesheet">
<style>
  :root{
    --paper:#f6f4ee;
    --ink:#1c1c1c;
    --red:#e0251b;
    --yellow:#fbe45a;
    --navy:#1c3e8c;
    --white:#ffffff;
  }
  *{margin:0;padding:0;box-sizing:border-box}
  html,body{width:752px;height:1200px;overflow:hidden;background:var(--paper)}
  .cover{position:relative;width:752px;height:1200px;background:var(--paper);
    font-family:"Noto Sans JP",sans-serif;color:var(--ink);overflow:hidden}

  .art-scale{position:absolute;left:540px;top:0;width:212px;height:170px;
    background:radial-gradient(ellipse at 60% 40%,#ffffff 0%,#e4e6ea 60%,#c9cdd3 100%);
    border-bottom-left-radius:110px}
  .art-people{position:absolute;left:40px;top:500px;width:470px;height:290px;
    background:linear-gradient(180deg,#f1e6da 0%,#e8d8c8 100%);border-radius:8px}

  .title-line{position:absolute;left:30px;font-family:"Noto Serif JP",serif;font-weight:900;
    white-space:nowrap;line-height:1.1}
  .title-line.one{top:50px;font-size:62px}
  .title-line.two{top:150px;font-size:64px}
  .bubble{position:absolute;left:404px;top:14px;width:150px;height:70px}
  .bubble svg{position:absolute;left:0;top:0}
  .bubble span{position:absolute;left:0;right:0;bottom:0;height:40px;display:flex;
    align-items:center;justify-content:center;font-size:26px;font-weight:700;line-height:1}

  .boxed{position:absolute;left:40px;top:295px;display:flex;gap:8px}
  .boxed span{width:128px;height:128px;border:3px solid var(--ink);background:var(--white);
    color:var(--red);font-size:100px;font-weight:900;display:flex;align-items:center;justify-content:center;line-height:1}

  .vertical{position:absolute;left:540px;top:300px;writing-mode:vertical-rl;
    font-size:180px;font-weight:900;line-height:1;letter-spacing:40px}

  .author{position:absolute;left:30px;top:800px}
  .author .role{font-family:"Noto Serif JP",serif;font-weight:900;font-size:36px;line-height:1.2}
  .author .role small{font-family:"Noto Sans JP",sans-serif;font-size:20px;font-weight:700;margin-left:8px}
  .author .org{font-size:20px;font-weight:700;margin-top:2px}
  .author .name{font-family:"Noto Serif JP",serif;font-weight:900;font-size:64px;letter-spacing:10px;
    display:flex;align-items:flex-end;line-height:1.1}
  .author .name .by{font-family:"Noto Sans JP",sans-serif;font-size:24px;font-weight:700;letter-spacing:0;
    border-left:2px solid var(--ink);padding-left:10px;margin-left:8px;margin-bottom:12px}

  .bonus{position:absolute;left:0;top:955px;width:752px;height:245px;background:var(--yellow)}
  .bonus .head{position:absolute;left:20px;top:4px;color:var(--red);font-size:40px;font-weight:900;line-height:1.3}
  .bonus .badge{position:absolute;left:420px;top:4px;width:86px;height:52px;background:var(--white);
    border:2px solid var(--ink);border-radius:10px;font-size:17px;font-weight:700;line-height:1.1;
    display:flex;flex-direction:column;align-items:center;justify-content:center}
  .gift{position:absolute;left:14px;background:var(--white);border-left:10px solid var(--navy);
    color:var(--navy);font-weight:900;padding:4px 14px 6px;line-height:1.25}
  .gift.first{top:60px}
  .gift.second{top:168px}
  .gift .lead{font-size:22px;font-weight:700}
  .gift .main{font-size:34px;display:flex;align-items:center;gap:6px}
  .gift .num{background:var(--navy);color:var(--white);width:38px;height:42px;
    display:inline-flex;align-items:center;justify-content:center;font-size:32px}
</style>
</head>
<body>
<div class="cover">
  <div class="art-scale" role="img" aria-label="体重計と巻き尺のイラスト"></div>

  <div class="title-line one">夜明けの庭で</div>
  <div class="bubble">
    <svg width="150" height="70" viewBox="0 0 150 70"><path d="M8 34 Q75 -6 142 34" fill="none" stroke="#1c1c1c" stroke-width="2.5"/></svg>
    <span>見つけた</span>
  </div>
  <div class="title-line two">静かな暮らしの</div>

  <div class="boxed"><span>小</span><span>さ</span><span>な</span></div>
  <div class="vertical">習慣</div>

  <div class="art-people" role="img" aria-label="様々な体型の男女が並ぶイラスト"></div>

  <div class="author">
    <div class="role">医師<small>循環器専門医</small></div>
    <div class="org">瑞穂橋文化振興会公認スポーツドクター</div>
    <div class="name">桐原晴臣<span class="by">著</span></div>
  </div>

  <div class="bonus">
    <div class="head">読者限定プレゼント</div>
    <div class="badge"><span>PDF</span><span>冊子</span></div>
    <div class="gift first">
      <div class="lead">減量したい人は是非</div>
      <div class="main">食べて欲しい食品ベスト<span class="num">5</span></div>
    </div>
    <div class="gift second">
      <div class="main">基礎代謝を上げる方法ベスト<span class="num">5</span></div>
    </div>
  </div>
</div>
</body>
</html>
```